Creating a website for a life changing company (Vantara Q)

We do need a website for our Coaching and Consulting business we recently launched. We do need it for information purposes and that our clients do have the opportunity to subscribe for packages, programs etc.
We would like to see designs which use the colours blue and yellow (see attachment). The final design should communicate our passion for the potential in people and the benefit (going beyond) for them.
Updates
Additional information:
Our company (webpage): Vantara Q (the C stands for "what people cannot see / imagine now...)
Welcome to Vantara Q(uest)
Consulting (O.R.B.) & Coaching (Rise onward)
Two pillars:
1) O.R.B. ( Leadership evolution - Our program - focussing on companies - business orientated)
2) Rise onward (Life transformation - Events - focusing on individuals - primarily life changing)
For both of them we offer: Concierge & Vantara Q+ (This should go as a subscription)
Eventually you can draft this as a rhombus
Industry/Entity Type
Coaching / Consulting
Coding
Coded - Design and coding required
Number of Pages Required
1 page
Font styles to use
Other font styles liked:
- Lato
Requirements
Must have
- Please see attachment (About us / Offers / Calendar function / Links to Instagram and LinkedIn account / mailing list / page for clients
Nice to have
- A banner

```html
<!DOCTYPE html>
<html lang="en">
<head>
<meta charset="utf-8">
<title>Vantara Q — Coaching &amp; Consulting</title>
<link href="https://fonts.googleapis.com/css2?family=Lato:wght@300;400;700&family=Poppins:wght@300;400;500;600&display=swap" rel="stylesheet">
<style>
:root{
  --navy:#0c3256;
  --navy-deep:#082744;
  --yellow:#fdd54b;
  --grey:#ebebeb;
  --white:#ffffff;
  --ink:#1d3a5c;
}
*{box-sizing:border-box;margin:0;padding:0}
html,body{width:1200px;height:5013px;overflow:hidden;background:var(--white)}
body{font-family:"Poppins",sans-serif;color:var(--navy)}
.page{position:relative;width:1200px;height:5013px;overflow:hidden}
.abs{position:absolute}
section,header,footer{position:absolute;left:0;width:1200px;overflow:hidden}
.btn{position:absolute;display:flex;align-items:center;justify-content:center;background:var(--yellow);color:var(--white);border-radius:30px;font-family:"Lato",sans-serif;font-size:15px;font-weight:400;letter-spacing:.3px;text-transform:uppercase}
.section-title{position:absolute;left:0;width:1200px;text-align:center;font-size:54px;font-weight:500;line-height:1}
.rule{position:absolute;height:3px;background:var(--yellow)}
.photo{position:absolute}

/* hero */
.hero{top:0;height:700px;background:var(--navy)}
.hero-yellow{left:600px;top:0;width:600px;height:700px;background:var(--yellow)}
.brand{position:absolute;font-family:"Poppins",sans-serif;font-weight:500;color:var(--white);letter-spacing:4px}
.nav a{position:absolute;top:70px;font-size:15px;color:var(--white);text-decoration:none;font-family:"Poppins",sans-serif}
.nav a.active{color:var(--yellow);text-decoration:underline}
.hero-title{left:84px;top:240px;font-family:"Lato",sans-serif;font-weight:300;font-size:60px;color:var(--white);letter-spacing:1px}
.hero-tag{left:88px;top:320px;font-size:29px;font-weight:500;color:var(--white)}
.hero-sub{left:88px;top:372px;font-size:18px;line-height:29px;color:var(--white);font-weight:300}

/* about */
.about{top:700px;height:681px;background:var(--white)}
.about-text{left:680px;top:275px;width:425px;text-align:center;font-size:13.5px;line-height:26px;color:var(--ink)}

/* orb */
.orb{top:1381px;height:797px;background:var(--grey)}
.orb-card{position:absolute;width:467px;height:171px;background:var(--white);border-radius:86px}
.orb-card h3{position:absolute;font-size:18px;font-weight:500;color:var(--navy);text-transform:uppercase}
.orb-card p{position:absolute;width:265px;font-size:13px;line-height:21px;color:#2d5a8a}
.orb-card svg{position:absolute}
.orb-word{position:absolute;left:0;width:1257px;top:358px;text-align:center;font-size:54px;font-weight:500;color:var(--yellow)}

/* concierge */
.concierge{top:2178px;height:915px;background:var(--white)}
.concierge-sub{left:0;width:1200px;top:197px;text-align:center;font-size:18px;line-height:25px;color:var(--navy)}
.offer-name{position:absolute;width:340px;text-align:center;font-size:30px;font-weight:500;color:var(--navy)}

/* rise onward */
.rise{top:3093px;height:709px;background:var(--navy)}
.rise-card{position:absolute;width:457px;height:183px;border:2px solid var(--yellow);border-radius:0 0 60px 0;overflow:hidden}
.rise-card .photo{left:0;top:0;width:224px;height:100%}
.rise-card h3{position:absolute;left:250px;top:30px;width:190px;font-size:18px;line-height:23px;font-weight:500;color:var(--yellow);text-transform:uppercase}
.rise-card p{position:absolute;left:250px;width:190px;font-size:12.5px;line-height:19px;color:var(--white)}

/* plus */
.plus{top:3802px;height:812px;background:var(--white)}
.step-num{position:absolute;width:86px;height:86px;border-radius:50%;display:flex;align-items:center;justify-content:center;font-size:38px;font-weight:500}
.step h3{position:absolute;left:760px;font-size:27px;font-weight:400;color:var(--yellow)}
.step p{position:absolute;left:760px;width:320px;font-size:15px;line-height:22px;color:var(--navy)}

/* footer */
.footer{top:4614px;height:399px;background:var(--navy);color:var(--white)}
.footer h4{position:absolute;top:68px;font-size:24px;font-weight:500}
.footer .link{position:absolute;font-size:13.5px;color:var(--white)}
.contact-line{position:absolute;left:945px;font-size:13px;line-height:18px;color:var(--white);width:150px}
.copyright{left:107px;top:326px;font-size:14px;color:var(--white)}
.social{position:absolute;top:310px;width:50px;height:50px;border-radius:50%;border:3px solid var(--white)}
</style>
</head>
<body>
<div class="page">

<!-- HERO -->
<header class="hero">
  <div class="abs hero-yellow"></div>
  <div class="abs" style="left:64px;top:78px;width:24px;height:2px;background:var(--white)"></div>
  <div class="brand" style="left:116px;top:66px;font-size:20px">VANTARA Q</div>
  <div class="abs" style="left:286px;top:78px;width:25px;height:2px;background:var(--white)"></div>
  <nav class="nav">
    <a class="active" style="left:418px">Vantara Q</a>
    <a style="left:517px">About Us</a>
    <a style="left:612px">O.R.B.</a>
    <a style="left:685px">Concierge</a>
    <a style="left:785px">Rise Onward</a>
    <a style="left:903px">Vantara Q+</a>
    <a style="left:1010px">Testimonials</a>
  </nav>
  <h1 class="abs hero-title">VANTARA Q</h1>
  <p class="abs hero-tag">We O.R.B. Your Company</p>
  <p class="abs hero-sub">We Ignite The Passion In people<br>To Unleash Their Full Potential</p>
  <div class="btn" style="left:91px;top:457px;width:210px;height:43px">Book your session</div>
  <div class="photo" role="img" aria-label="Photo of two business people smiling at each other across a laptop" style="left:473px;top:165px;width:669px;height:434px;border-radius:120px 0 90px 0;background:linear-gradient(120deg,#c9a24a 0%,#8a6d45 35%,#3b4656 65%,#1d2c42 100%)"></div>
</header>

<!-- ABOUT -->
<section class="about">
  <svg class="abs" style="left:0;top:300px" width="45" height="115" viewBox="0 0 45 115"><polygon points="0,0 43,16 20,115 0,108" fill="var(--navy)"/></svg>
  <svg class="abs" style="left:1100px;top:30px" width="100" height="220" viewBox="0 0 100 220"><circle cx="100" cy="117" r="84" fill="none" stroke="var(--yellow)" stroke-width="24"/></svg>

  <div class="abs" style="left:98px;top:170px;width:232px;height:335px;border:2px solid var(--yellow);border-radius:40px 0 116px 116px"></div>
  <svg class="abs" style="left:110px;top:395px" width="250" height="160" viewBox="0 0 250 160"><path d="M14 20 A112 112 0 0 0 236 20" fill="none" stroke="var(--yellow)" stroke-width="24"/></svg>
  <div class="photo" role="img" aria-label="Portrait of a coach in a blue suit" style="left:123px;top:185px;width:229px;height:327px;border-radius:0 0 114px 114px;background:linear-gradient(160deg,#1f4c85 0%,#2c5f9e 45%,#e2d9cc 75%,#0e2c50 100%)"></div>

  <svg class="abs" style="left:395px;top:200px" width="200" height="90" viewBox="0 0 200 90"><path d="M14 86 A86 86 0 0 1 186 86" fill="none" stroke="var(--yellow)" stroke-width="26"/></svg>
  <div class="abs" style="left:395px;top:200px;width:230px;height:375px;border:2px solid var(--yellow);border-radius:115px 115px 0 0"></div>
  <div class="photo" role="img" aria-label="Portrait of a coach holding an umbrella outdoors" style="left:370px;top:230px;width:227px;height:325px;border-radius:114px 114px 0 0;background:linear-gradient(150deg,#3f9fa3 0%,#2d6b64 40%,#607a4a 70%,#2a3a2c 100%)"></div>

  <div class="rule" style="left:690px;top:216px;width:49px"></div>
  <h2 class="abs" style="left:740px;top:188px;width:285px;text-align:center;font-size:54px;font-weight:500;line-height:1">About Us</h2>
  <div class="rule" style="left:1025px;top:216px;width:49px"></div>
  <p class="abs about-text">Welcome to Vantara Q, where Passion for igniting People's Potential is in our DNA and brought Us together. The journey starts in the Himalayas to Everest Base Camp, where transformation happened for both of them, it was going Beyond (Q) what they could see, comprehend and imagine.</p>
  <div class="btn" style="left:688px;top:436px;width:401px;height:43px">Learn more about Marek and Lena</div>
</section>

<!-- O.R.B. -->
<section class="orb">
  <circle></circle>
  <svg class="abs" style="left:338px;top:101px" width="582" height="582" viewBox="0 0 582 582">
    <circle cx="291" cy="291" r="290" fill="var(--yellow)"/>
    <ellipse cx="291" cy="292" rx="280" ry="203" fill="var(--navy)"/>
  </svg>
  <div class="rule" style="left:451px;top:393px;width:49px"></div>
  <div class="orb-word">O.R.B.</div>
  <div class="rule" style="left:702px;top:393px;width:49px"></div>

  <div class="orb-card" style="left:80px;top:189px">
    <svg style="left:58px;top:45px" width="80" height="80" viewBox="0 0 80 80" fill="none" stroke="var(--navy)" stroke-width="3">
      <circle cx="18" cy="30" r="8"/><path d="M4 58 q14-20 28 0z"/><path d="M32 40 h10 M42 18 v44 M42 18 h12 M42 40 h12 M42 62 h12"/>
      <circle cx="64" cy="18" r="7"/><rect x="57" y="34" width="14" height="12"/><circle cx="64" cy="62" r="7"/>
    </svg>
    <h3 style="left:185px;top:52px">Leadership Evolution</h3>
    <p style="left:185px;top:84px">Lorem ipsum dolor sitm ipsum dolor sloat consectetur adipiscim ipsumtng.</p>
  </div>
  <div class="orb-card" style="left:654px;top:189px">
    <svg style="left:43px;top:40px" width="95" height="95" viewBox="0 0 95 95" fill="none" stroke="var(--navy)" stroke-width="3">
      <circle cx="44" cy="50" r="38"/><circle cx="44" cy="50" r="26"/><circle cx="44" cy="50" r="14"/><circle cx="44" cy="50" r="4" fill="var(--navy)"/>
      <path d="M44 50 L82 12 M74 10 l8 2 l2 8"/>
    </svg>
    <h3 style="left:163px;top:52px">Focussing on Companies</h3>
    <p style="left:163px;top:84px">Lorem ipsum dolor sitm ipsum dolor sloat consectetur adipiscim ipsumtng.</p>
  </div>
  <div class="orb-card" style="left:80px;top:422px">
    <svg style="left:55px;top:40px" width="100" height="90" viewBox="0 0 100 90" fill="none" stroke="var(--navy)" stroke-width="3">
      <circle cx="52" cy="30" r="12"/><circle cx="52" cy="30" r="22" stroke-dasharray="6 5"/>
      <path d="M6 62 q20-10 40 2 h20 q6 4 0 8 h-24 M46 72 q22 6 44-12 q-6-6-14 0"/><path d="M6 62 v24"/>
    </svg>
    <h3 style="left:185px;top:52px">Our Program</h3>
    <p style="left:185px;top:84px">Lorem ipsum dolor sitm ipsum dolor sloat consectetur adipiscim ipsumtng.</p>
  </div>
  <div class="orb-card" style="left:654px;top:422px">
    <svg style="left:45px;top:40px" width="95" height="95" viewBox="0 0 95 95" fill="none" stroke="var(--navy)" stroke-width="3">
      <circle cx="47" cy="30" r="11"/><path d="M30 70 v-16 q17-14 34 0 v16 M38 70 v16 M56 70 v16"/>
      <path d="M8 8 l12 12 M8 8 h8 M8 8 v8 M86 8 l-12 12 M86 8 h-8 M86 8 v8 M8 86 l12-12 M8 86 h8 M8 86 v-8 M86 86 l-12-12 M86 86 h-8 M86 86 v-8 M2 48 h18 M74 48 h18"/>
    </svg>
    <h3 style="left:169px;top:52px">Business Orientated</h3>
    <p style="left:169px;top:84px">Lorem ipsum dolor sitm ipsum dolor sloat consectetur adipiscim ipsumtng.</p>
  </div>
</section>

<!-- CONCIERGE -->
<section class="concierge">
  <svg class="abs" style="left:1060px;top:40px" width="140" height="240" viewBox="0 0 140 240"><circle cx="140" cy="110" r="96" fill="none" stroke="var(--navy)" stroke-width="26"/></svg>
  <div class="rule" style="left:391px;top:135px;width:52px"></div>
  <h2 class="section-title" style="top:108px">Concierge</h2>
  <div class="rule" style="left:757px;top:135px;width:52px"></div>
  <p class="abs concierge-sub">Concierge package offers you an&nbsp; ongoing partnership as you<br>navigate your&nbsp; journey to reach your full potential</p>

  <svg class="abs" style="left:79px;top:307px" width="340" height="340" viewBox="0 0 340 340"><circle cx="170" cy="170" r="164" fill="none" stroke="var(--yellow)" stroke-width="10" stroke-dasharray="620 410" transform="rotate(200 170 170)"/></svg>
  <div class="photo" role="img" aria-label="Photo of a coach talking with a client by a window" style="left:97px;top:325px;width:304px;height:304px;border-radius:50%;background:linear-gradient(135deg,#e6e4de 0%,#b9c2cc 40%,#8a6a55 75%,#5b4436 100%)"></div>
  <div class="offer-name" style="left:79px;top:660px">Coaching</div>

  <svg class="abs" style="left:429px;top:307px" width="340" height="340" viewBox="0 0 340 340"><circle cx="170" cy="170" r="164" fill="none" stroke="var(--yellow)" stroke-width="10" stroke-dasharray="600 430" transform="rotate(160 170 170)"/></svg>
  <div class="photo" role="img" aria-label="Photo of two consultants in suits working at a laptop" style="left:447px;top:325px;width:304px;height:304px;border-radius:50%;background:linear-gradient(135deg,#d6d8dc 0%,#8b9096 35%,#1f2836 70%,#3c3f47 100%)"></div>
  <div class="offer-name" style="left:429px;top:660px">Consulting</div>

  <svg class="abs" style="left:773px;top:307px" width="340" height="340" viewBox="0 0 340 340"><circle cx="170" cy="170" r="164" fill="none" stroke="var(--yellow)" stroke-width="10" stroke-dasharray="560 470" transform="rotate(120 170 170)"/></svg>
  <div class="photo" role="img" aria-label="Photo of hands holding a phone with chat bubbles" style="left:791px;top:325px;width:304px;height:304px;border-radius:50%;background:linear-gradient(135deg,#d9b48a 0%,#c48a5a 40%,#8f5a3a 75%,#6a3f2a 100%)"></div>
  <div class="offer-name" style="left:773px;top:660px">Fireside Chat</div>

  <div class="btn" style="left:508px;top:747px;width:184px;height:45px">Subscribe us</div>
  <svg class="abs" style="left:155px;top:805px" width="220" height="110" viewBox="0 0 220 110"><circle cx="110" cy="112" r="96" fill="none" stroke="var(--yellow)" stroke-width="26"/></svg>
</section>

<!-- RISE ONWARD -->
<section class="rise">
  <div class="rule" style="left:373px;top:97px;width:51px"></div>
  <h2 class="section-title" style="top:70px;color:var(--white)">Rise Onward</h2>
  <div class="rule" style="left:778px;top:97px;width:51px"></div>

  <div class="rise-card" style="left:99px;top:182px">
    <div class="photo" role="img" aria-label="Photo of a wooden signpost at sunset" style="background:linear-gradient(135deg,#f3cfa2 0%,#d99a6a 45%,#8a5a40 100%)"></div>
    <h3>Life<br>Transformation</h3>
    <p style="top:90px">Lorem ipsum dolor sit amet, incididunt ut ma aliqua. ........</p>
  </div>
  <div class="rise-card" style="left:605px;top:182px">
    <div class="photo" role="img" aria-label="Photo of a group of people at an event" style="background:linear-gradient(135deg,#6b5a52 0%,#a69b94 45%,#3e4652 100%)"></div>
    <h3>Events</h3>
    <p style="top:67px">Lorem ipsum dolor sit amet, incididunt ut ma aliqua. ........</p>
  </div>
  <div class="rise-card" style="left:99px;top:408px">
    <div class="photo" role="img" aria-label="Photo of a person facing a golden sunrise" style="background:linear-gradient(135deg,#2c2a26 0%,#8a6a3a 45%,#f1c56a 75%,#b28445 100%)"></div>
    <h3>Focusing on<br>Individuals</h3>
    <p style="top:90px">Lorem ipsum dolor sit amet, incididunt ut ma aliqua. ........</p>
  </div>
  <div class="rise-card" style="left:605px;top:408px">
    <div class="photo" role="img" aria-label="Photo of a person jumping above the sea" style="background:linear-gradient(180deg,#bfe3f0 0%,#5fb3d6 50%,#1f7fb0 100%)"></div>
    <h3>Primarily Life<br>Changing</h3>
    <p style="top:90px">Lorem ipsum dolor sit amet, incididunt ut ma aliqua. ........</p>
  </div>
</section>

<!-- VANTARA Q+ -->
<section class="plus">
  <div class="rule" style="left:373px;top:127px;width:51px"></div>
  <h2 class="section-title" style="top:100px">Vantara Q+</h2>
  <div class="rule" style="left:778px;top:127px;width:51px"></div>

  <div class="photo" role="img" aria-label="Photo of a coach in conversation with a client taking notes" style="left:99px;top:224px;width:463px;height:473px;border-radius:88px 20px 88px 88px;background:linear-gradient(135deg,#eceae4 0%,#bcc6d0 40%,#8a6a55 75%,#5b4436 100%)"></div>

  <div class="step">
    <div class="step-num" style="left:644px;top:222px;background:var(--navy);color:var(--white)">1</div>
    <h3 style="top:232px">Coaching Insights</h3>
    <p style="top:273px">Become familiar with the insights and<br>&nbsp;principles of coaching and<br>&nbsp;understand their benifits</p>
  </div>
  <div class="step">
    <div class="step-num" style="left:644px;top:372px;border:2px solid var(--navy);color:var(--navy)">2</div>
    <h3 style="top:383px">Grab and Go</h3>
    <p style="top:424px">Invitation to grab valuable tips to make a<br>change in your life!</p>
  </div>
  <div class="step">
    <div class="step-num" style="left:644px;top:506px;border:2px solid var(--navy);color:var(--navy)">3</div>
    <h3 style="top:518px">Be Resourceful</h3>
    <p style="top:559px">Pay attention to the valuable resources<br>which you could benefit from</p>
  </div>
  <div class="btn" style="left:646px;top:654px;width:184px;height:45px">Subscribe us</div>
</section>

<!-- FOOTER -->
<footer class="footer">
  <h4 style="left:150px">Explore</h4>
  <span class="link" style="left:152px;top:126px">Vantara Q</span>
  <span class="link" style="left:152px;top:155px">About Us</span>
  <span class="link" style="left:155px;top:186px">O.R.B.</span>
  <span class="link" style="left:152px;top:217px">Concierge</span>
  <span class="link" style="left:266px;top:126px">Rise Onward</span>
  <span class="link" style="left:266px;top:155px">Vantara Q+</span>
  <span class="link" style="left:266px;top:186px">Testimonials</span>

  <div class="abs" style="left:445px;top:152px;width:37px;height:2px;background:var(--white)"></div>
  <div class="brand" style="left:500px;top:136px;font-size:26px;width:265px;text-align:center">VANTARA Q</div>
  <div class="abs" style="left:780px;top:152px;width:37px;height:2px;background:var(--white)"></div>

  <h4 style="left:899px">Contact Us</h4>
  <svg class="abs" style="left:898px;top:126px" width="32" height="32" viewBox="0 0 32 32" fill="none" stroke="var(--yellow)" stroke-width="2"><circle cx="16" cy="16" r="15"/><path d="M16 25 q-7-8-7-12 a7 7 0 0 1 14 0 q0 4-7 12z"/><circle cx="16" cy="13" r="2.5"/></svg>
  <p class="contact-line" style="top:124px">123 ipsum dolor sit amet, consectetur adipiscing elit</p>
  <svg class="abs" style="left:898px;top:186px" width="32" height="32" viewBox="0 0 32 32" fill="none" stroke="var(--yellow)" stroke-width="2"><circle cx="16" cy="16" r="15"/><path d="M11 9 l3 0 l1.5 4 l-2 1.5 q1.5 3 4 4.5 l1.5-2 l4 1.5 v3 q-1 1.5-3 1.5 q-10-2-12-12 q0-2 3-2z"/></svg>
  <p class="contact-line" style="top:193px">+000 555 0142</p>
  <svg class="abs" style="left:898px;top:232px" width="32" height="32" viewBox="0 0 32 32" fill="none" stroke="var(--yellow)" stroke-width="2"><circle cx="16" cy="16" r="15"/><rect x="9" y="11" width="14" height="10"/><path d="M9 11 l7 6 l7-6"/></svg>
  <p class="contact-line" style="top:239px;width:230px">hello@vantaraq.example</p>

  <p class="abs copyright">© 2022&nbsp; VANTARA Q.ALL RIGHTS RESERVED</p>
  <div class="social" role="img" aria-label="Professional network profile link" style="left:977px"></div>
  <div class="social" role="img" aria-label="Photo sharing profile link" style="left:1047px"></div>
</footer>

</div>
</body>
</html>
```